Fiber Optic Internet flyer promotion Winter 2016-2017

I am looking for a marketing flyer that will not be folded, single sided that will advertise a Fiber Optic internet promotion that we are currently running.

The design should be clean, flow well, quickly grab attention, and if a very few short seconds list what the promotion is, and direct them to contact us.

It needs to list a few features of the promotion, but does not need to be in this order and should flow well with the flyer
1.) Fiber Optic Internet
2.) 100 Mbits for $140 /month or 150 Mbits for $190 /month
3.) Free construction cost up to $10,000, limited funds available.
4.) Limited time offer. Must commit before funds run out.

(555) 274-3916, www.kelvoranet.example

Target Market(s)

Small to large business

Industry/Entity Type

Internet Service Provider

Requirements
Must have
• Eye catching appeal. Quickly convey the message of the promotion and our company name and phone number.
Should not have
• Our company is primarily a wireless ISP. This promotion is all about Fiber Optic. I do not want to draw attention to the "wireless" portion of our business with this flyer.

```html
<!DOCTYPE html>
<html lang="en">
<head>
<meta charset="utf-8">
<title>Fiber Optic Internet – Limited Time Offer</title>
<link rel="stylesheet" href="https://fonts.googleapis.com/css2?family=Roboto+Condensed:wght@400;700&family=Audiowide&family=Roboto:wght@700;900&display=swap">
<style>
  :root {
    --navy: #13167a;
    --navy-deep: #0c0f5c;
    --band-blue: #6d7ff2;
    --yellow: #f8d848;
    --red: #a3191b;
    --white: #ffffff;
    --footer-grey: #4b4b4e;
    --photo-dark: #2a2230;
    --photo-mid: #6b5a6e;
    --photo-light: #b7a2b0;
  }
  html, body {
    margin: 0;
    padding: 0;
    overflow: hidden;
    background: #e9e9e9;
  }
  .flyer {
    position: relative;
    width: 859px;
    height: 1200px;
    overflow: hidden;
    background: var(--navy);
    font-family: "Roboto Condensed", "Arial Narrow", sans-serif;
    color: var(--white);
  }
  .backdrop {
    position: absolute;
    inset: 0;
    width: 859px;
    height: 1200px;
  }
  .headline-small {
    position: absolute;
    left: 46px;
    top: 46px;
    margin: 0;
    font-weight: 400;
    font-size: 76px;
    line-height: 1;
    letter-spacing: 1px;
  }
  .headline-large {
    position: absolute;
    left: 42px;
    top: 160px;
    margin: 0;
    font-family: "Audiowide", sans-serif;
    font-weight: 400;
    font-size: 104px;
    line-height: 1;
    letter-spacing: -2px;
    background: linear-gradient(180deg, #ffffff 0%, #d9d9de 45%, #8d8d96 55%, #f3f3f6 100%);
    -webkit-background-clip: text;
    background-clip: text;
    color: transparent;
    filter: drop-shadow(2px 4px 3px rgba(0,0,0,0.55));
  }
  .offer {
    position: absolute;
    right: 14px;
    top: 612px;
    text-align: right;
  }
  .offer-kicker {
    font-weight: 700;
    font-size: 38px;
    line-height: 1;
  }
  .offer-title {
    font-weight: 700;
    font-size: 88px;
    line-height: 0.95;
    color: var(--yellow);
    margin-top: 4px;
  }
  .offer-terms {
    font-weight: 400;
    font-size: 26px;
    line-height: 36px;
    margin-top: 6px;
  }
  .plan {
    position: absolute;
    left: 30px;
  }
  .plan-speed {
    display: flex;
    align-items: center;
    font-family: "Roboto", sans-serif;
    font-weight: 900;
    font-size: 66px;
    line-height: 1;
    letter-spacing: 1px;
  }
  .plan-for {
    margin-left: 10px;
    width: 26px;
    height: 56px;
    background: var(--red);
    display: flex;
    align-items: center;
    justify-content: center;
  }
  .plan-for span {
    display: block;
    transform: rotate(-90deg);
    font-family: "Roboto Condensed", sans-serif;
    font-weight: 700;
    font-size: 20px;
    letter-spacing: 1px;
  }
  .plan-price {
    font-weight: 700;
    font-size: 58px;
    line-height: 1;
    color: var(--yellow);
    margin-top: 6px;
  }
  .plan-one { top: 792px; }
  .plan-two { top: 1010px; }
  .plan-or {
    position: absolute;
    left: 24px;
    top: 930px;
    width: 70px;
    height: 56px;
    border-radius: 50%;
    background: var(--red);
    font-weight: 700;
    font-size: 38px;
    line-height: 56px;
    text-align: center;
  }
  .contact-card {
    position: absolute;
    left: 455px;
    top: 883px;
    width: 404px;
    height: 236px;
  }
  .contact-card svg { position: absolute; inset: 0; }
  .brand {
    position: absolute;
    left: 0;
    right: 14px;
    top: 50px;
    display: flex;
    align-items: center;
    justify-content: center;
    gap: 12px;
    font-weight: 700;
    font-size: 40px;
    letter-spacing: 1px;
    color: var(--navy);
  }
  .brand-dot {
    width: 30px;
    height: 30px;
    border-radius: 50%;
    background: var(--red);
  }
  .contact-line {
    position: absolute;
    display: flex;
    align-items: center;
    gap: 10px;
    font-family: "Roboto", sans-serif;
    font-weight: 900;
    color: var(--white);
    letter-spacing: 1.5px;
  }
  .contact-phone { left: 50px; top: 150px; font-size: 22px; }
  .contact-web { left: 62px; top: 194px; font-size: 18px; letter-spacing: 1px; }
  .contact-line svg { position: static; }
  .footer {
    position: absolute;
    left: 0;
    right: 0;
    bottom: 0;
    height: 50px;
    border-top: 5px solid var(--white);
    background: var(--footer-grey);
    font-weight: 400;
    font-size: 24px;
    line-height: 50px;
    text-align: center;
    letter-spacing: 0.5px;
  }
</style>
</head>
<body>
  <main class="flyer">
    <svg class="backdrop" viewBox="0 0 859 1200" aria-hidden="true">
      <defs>
        <radialGradient id="photoGlow" cx="0.7" cy="0.55" r="0.75">
          <stop offset="0" stop-color="#efe6f0"/>
          <stop offset="0.3" stop-color="#b7a2b0"/>
          <stop offset="0.65" stop-color="#6b5a6e"/>
          <stop offset="1" stop-color="#2a2230"/>
        </radialGradient>
        <linearGradient id="navyFade" x1="0" y1="0" x2="1" y2="1">
          <stop offset="0" stop-color="#161a86"/>
          <stop offset="1" stop-color="#0c0f5c"/>
        </linearGradient>
      </defs>
      <rect x="0" y="0" width="859" height="1200" fill="url(#navyFade)"/>
      <rect role="img" aria-label="Photograph of a fiber optic cable with coloured tubes and glowing light strands over a dark bokeh background" x="0" y="0" width="859" height="800" fill="url(#photoGlow)"/>
      <path d="M0 545 C 40 640, 90 745, 170 762 C 300 790, 600 620, 859 500 L 859 1200 L 0 1200 Z" fill="var(--band-blue)"/>
      <path d="M0 572 C 40 660, 95 760, 180 776 C 320 800, 610 640, 859 528 L 859 1200 L 0 1200 Z" fill="url(#navyFade)"/>
    </svg>

    <h1 class="headline-small">Fiber Optic</h1>
    <h2 class="headline-large">INTERNET</h2>

    <section class="offer">
      <div class="offer-kicker">LIMITED TIME</div>
      <div class="offer-title">OFFER</div>
      <div class="offer-terms">MUST COMMIT<br>BEFORE FUNDS<br>RUN OUT.</div>
    </section>

    <section class="plan plan-one">
      <div class="plan-speed">100 MBITS<span class="plan-for"><span>FOR</span></span></div>
      <div class="plan-price">$140 / MONTH</div>
    </section>
    <div class="plan-or">OR</div>
    <section class="plan plan-two">
      <div class="plan-speed">150 MBITS<span class="plan-for"><span>FOR</span></span></div>
      <div class="plan-price">$190 / MONTH</div>
    </section>

    <section class="contact-card">
      <svg width="404" height="236" viewBox="0 0 404 236" aria-hidden="true">
        <path d="M28 0 H404 V236 H90 C 70 236, 58 226, 52 210 L 2 30 C -3 12, 10 0, 28 0 Z" fill="var(--white)"/>
        <path d="M10 150 L 370 150 L 382 182 L 22 182 Z" fill="var(--red)"/>
        <path d="M30 193 L 378 193 L 390 225 L 42 225 Z" fill="var(--red)"/>
      </svg>
      <div class="brand"><span class="brand-dot"></span>KELVORA NET</div>
      <div class="contact-line contact-phone">
        <svg width="22" height="22" viewBox="0 0 24 24" aria-hidden="true"><circle cx="12" cy="12" r="12" fill="#fff"/><path d="M8 6c1 0 2 2 2 3s-1 1-1 2 3 4 4 4 1-1 2-1 3 1 3 2-1 3-3 3C10 19 5 14 5 9c0-2 2-3 3-3z" fill="var(--red)"/></svg>
        (555) 274-3916
      </div>
      <div class="contact-line contact-web">
        <svg width="18" height="18" viewBox="0 0 24 24" aria-hidden="true"><circle cx="12" cy="12" r="10" fill="none" stroke="#fff" stroke-width="2"/><ellipse cx="12" cy="12" rx="4" ry="10" fill="none" stroke="#fff" stroke-width="2"/><line x1="2" y1="12" x2="22" y2="12" stroke="#fff" stroke-width="2"/></svg>
        www.kelvoranet.example
      </div>
    </section>

    <footer class="footer">FREE CONSTRUCTION COST UP TO $10,000, LIMITED FUNDS AVAILABLE.</footer>
  </main>
</body>
</html>
```